Lanternis in a league of it's own

Lanternis is a pan European contact center.
We serve our clients in 18 languages from Antwerp in Belgium, Fez in Morocco and with our partner Velomreach.
We have a presentation and we would like to make it much more visible;
Less text, more images or animation.
Our business case is based on three elements with three colours :
blue sky : because we ar fully organized in the cloud,
Green : in our customer care college, out green village we put a lot of energy in training,
Orange : when technology is good and people have a good knowledge, passion will come...
Eventually we are ready to payfor some stock images - to negotiate-
For answers to your questions : tomas.verlaek@quillnet.be

```html
<!DOCTYPE html>
<html lang="en">
<head>
<meta charset="utf-8">
<title>Lanternis – Presentation</title>
<link href="https://fonts.googleapis.com/css2?family=Ubuntu:wght@300;400;500;700&display=swap" rel="stylesheet">
<style>
:root{
  --bg:#d9d9d9;
  --paper:#ffffff;
  --green:#8cc63f;
  --orange:#e8562a;
  --blue:#1a9ad6;
  --navy:#25344f;
  --ink:#4a4a4a;
  --muted:#7a7a7a;
  --red:#d9342b;
}
*{box-sizing:border-box;margin:0;padding:0}
html,body{width:1200px;height:783px;overflow:hidden}
body{background:var(--bg);font-family:"Ubuntu",sans-serif;color:var(--ink);position:relative}
.slide{position:absolute;width:370px;height:213px;background:var(--paper);box-shadow:0 1px 4px rgba(0,0,0,.25);overflow:hidden}
.s1{left:24px;top:38px}.s2{left:415px;top:38px}.s3{left:806px;top:38px}
.s4{left:24px;top:285px}.s5{left:415px;top:285px}.s6{left:806px;top:285px}
.s7{left:182px;top:531px}.s8{left:595px;top:531px}
.section-band{position:absolute;left:0;top:14px;width:98px;height:10px;background:var(--green);color:#fff;font-size:7px;font-weight:500;line-height:10px;padding-left:6px;clip-path:polygon(0 0,90% 0,100% 100%,0 100%)}
.sub-band{position:absolute;left:0;top:25px;width:180px;height:7px;background:var(--orange);color:#fff;font-size:4px;line-height:7px;padding-left:6px;clip-path:polygon(0 0,96% 0,100% 100%,0 100%);white-space:nowrap;overflow:hidden}
.brand{position:absolute;right:22px;top:16px;display:flex;align-items:center;gap:3px;font-size:12px;font-weight:400;color:var(--ink)}
.brand-dot{width:13px;height:13px;border-radius:50%;background:var(--orange)}
.footer{position:absolute;left:0;right:0;bottom:0;height:2px;background:linear-gradient(90deg,var(--orange) 0 33.3%,var(--green) 33.3% 66.6%,var(--blue) 66.6%)}
.page-no{position:absolute;right:8px;bottom:4px;font-size:5px;color:var(--muted)}
.txt{position:absolute;font-size:4px;line-height:1.45;color:var(--ink)}
.label-blue{color:var(--blue);font-size:5px}
.label-green{color:var(--green);font-size:5px}
.hl{color:var(--orange)}
.center{text-align:center}
.check{display:flex;align-items:center;gap:3px}
.check::before{content:"";width:12px;height:1px;background:var(--green)}
ul.bullets{list-style:none}
ul.bullets li::before{content:"• ";color:var(--green)}
.photo-circle{position:absolute;left:22px;top:60px;width:94px;height:94px;border-radius:50%;border:2px solid var(--orange);background:radial-gradient(circle at 40% 40%,#e9eef2,#9fb7c8 70%,#5b7e97)}
.photo-side{position:absolute;right:0;top:0;width:110px;height:213px;background:linear-gradient(160deg,#8fc4dc,#3e86aa 55%,#1f5e83);clip-path:polygon(30% 0,100% 0,100% 100%,0 100%)}
.heading-orange{position:absolute;left:140px;top:56px;font-size:6.5px;color:var(--orange);line-height:1.3}
.biz-row{position:absolute;left:30px;top:163px;display:flex;gap:10px}
.biz-btn{width:54px;height:16px;background:var(--blue);color:#fff;font-size:4px;display:flex;align-items:center;justify-content:center}
.quote-bar{position:absolute;left:18px;top:53px;width:1.5px;height:55px;background:var(--blue)}
.donut-label{position:absolute;left:300px;top:135px;font-size:3.5px;font-weight:700;text-align:center;width:30px;line-height:1.2}
.cop{position:absolute;left:0;right:0;top:148px;text-align:center;font-size:13px;color:var(--ink)}
.cop-sub{position:absolute;left:0;right:0;top:190px;text-align:center;font-size:6px;color:var(--orange)}
</style>
</head>
<body>

<!-- 1 -->
<section class="slide s1">
  <div class="section-band">1. STRATEGY</div>
  <div class="sub-band">a. People Business: review approach of the contact center agent. The agent dies, the advisors born.</div>
  <div class="brand"><span class="brand-dot"></span>Lanternis</div>
  <div class="txt" style="left:26px;top:54px"><span class="label-blue">Situation today:</span></div>
  <div class="txt center" style="left:20px;top:66px;width:90px">churn in contact centers is too important<br>high costs of training<br>low quality of service<br><span class="label-blue">=</span><br>client is not willing to pay for churn,<br>training, low quality<br>low satisfaction</div>
  <div class="txt center" style="left:135px;top:66px;width:100px">Contact Center Business<br><span class="label-blue">=</span><br>people business<br>invest again in people in the long run. Get<br>good people in and keep them in.</div>
  <div class="txt center" style="left:262px;top:66px;width:90px">Good people, good training<br><span class="label-blue">=</span><br>quality of services rendered.</div>
  <div class="txt" style="left:20px;top:118px">
    <div class="check">Clients are ready to pay for quality.</div>
    <div class="check">HR setup is based on good feeling and well-being of the advisor.</div>
    <div class="check">Increasement of productivity by individual and group motivation.</div>
  </div>
  <div class="txt" style="left:26px;top:150px"><span class="label-blue">The Customer Care College:</span><br>
  <span style="padding-left:12px">subsidized training academy which invests in training of advisors, team managers and client directors.</span><br>
  <span style="padding-left:12px">Train people through basic and advanced skill and product oriented training programs.</span></div>
  <div class="footer"></div><div class="page-no">1</div>
</section>

<!-- 2 -->
<section class="slide s2">
  <div class="section-band">1. STRATEGY</div>
  <div class="sub-band" style="width:120px">b. Technology.</div>
  <div class="brand"><span class="brand-dot"></span>Lanternis</div>
  <div class="photo-circle" role="img" aria-label="Photo of a contact center advisor wearing a headset"></div>
  <div class="heading-orange">In the Belgian market we see over loaded<br>and over sized supporting divisions in contact centers:</div>
  <div class="txt" style="left:150px;top:76px;width:200px">capex and opex-figures are much too high.<br>The contact center of the future is virtually organized in the cloud and stands for accessibility<br>without restrictions through homeworkers, offshore and nearshore service.<br>In order to be competitive we need to create a white paper philosophy, i.e. to start from scratch.<br>Don't invest in expensive infrastructure but use existing and proven systems.</div>
  <div class="txt" style="left:150px;top:112px;width:200px">Be aware of new technologies, solutions and other new market opportunities that can make the business grow.
  <ul class="bullets">
    <li>Telemonitoring and Medical Care : potential of the future,</li>
    <li>3D Website communication : live agents will interfere in e-commerce websites.</li>
    <li>Gamification : implementation of gamification to increase group productivity.</li>
    <li>Third party products : installation of third party solutions and work on call avoidance, call reduction time,<br>lower and minimize the 10 triggers that cause calls.</li>
  </ul></div>
  <div class="footer"></div><div class="page-no">2</div>
</section>

<!-- 3 -->
<section class="slide s3">
  <div class="section-band">1. STRATEGY</div>
  <div class="sub-band" style="width:160px">c. Environment and place to work.</div>
  <div class="photo-side" role="img" aria-label="Photo of a bright modern office interior with a round meeting table"></div>
  <div class="txt" style="left:12px;top:52px;width:220px;font-size:4.5px">Try to create a place where people feel good : people have to love their work environment.<br>A large area with a lot of light, fresh air and space.<br>Advisors are no laying hens, but people.<br>We look for landscape office that can fulfill these demands.<br>Our first location : Meridian Tower - Kaailaan 14 - Antwerp.
  <ul class="bullets" style="margin:3px 0 3px 6px"><li>Super facility.</li><li>Servihold facilities.</li></ul>
  Accessibility to public transportation is a must.<br>Location : Customer Care College: province of Limburg.
  <ul class="bullets" style="margin:3px 0 0 6px"><li>Contact Center : city of Antwerp.</li></ul></div>
  <div class="footer"></div><div class="page-no" style="color:#fff">3</div>
</section>

<!-- 4 -->
<section class="slide s4">
  <div class="section-band">1. STRATEGY</div>
  <div class="sub-band" style="width:140px">d. Cash generating oriented.</div>
  <div class="brand"><span class="brand-dot"></span>Lanternis</div>
  <div class="txt" style="left:22px;top:57px;width:300px;font-size:4.3px;line-height:1.5">
    By changing the investment policy, capex can be kept low and opex will follow.<br>No limits by trade unions, no seniority, lower overhead by co-using of supporting services.<br><br>
    With this offered business model, the selling price will remain identical towards clients.<br><br>
    The extra generated money will partly be invested in education, fixed contracts for the people and different profile of the teamcoach:<br>they become teammanagers.<br><br>
    We look for a mix of big clients <span class="hl">(100 advisors)</span> and semi big clients <span class="hl">(from 20 advisors)</span>.<br><br>
    Lots of semi big clients take care of a widespread portfolio.<br>
    <span class="label-blue" style="font-size:6px">Type of business :</span>
  </div>
  <div class="biz-row">
    <div class="biz-btn">INBOUND</div><div class="biz-btn">OUTBOUND</div><div class="biz-btn">ADMIN</div><div class="biz-btn">WEBCARE</div><div class="biz-btn">BPO</div>
  </div>
  <div class="footer"></div><div class="page-no">4</div>
</section>

<!-- 5 -->
<section class="slide s5">
  <div class="section-band">1. STRATEGY</div>
  <div class="sub-band" style="width:120px">e. Client oriented.</div>
  <div class="brand"><span class="brand-dot"></span>Lanternis</div>
  <div class="quote-bar"></div>
  <div class="txt" style="left:24px;top:54px;width:320px;font-size:4.3px;line-height:1.6">
    In this new strategy the client will be the central party and a very important stakeholder.<br><br>
    Good quality assures satisfied clients. Good quality is guaranteed by good advisors. Good advisors must receive a fair salary.<br><br>
    <span class="label-green">Flexibility.</span><br>
    Flexibility is the holy bible of the future contact center.<br><br>
    The new strategy and the new model have no past, no history and can organize the contact center business towards the needs of the client.
  </div>
  <div class="footer"></div><div class="page-no">5</div>
</section>

<!-- 6 -->
<section class="slide s6">
  <div class="section-band">2.OPERATIONS</div>
  <div class="sub-band" style="width:120px">a. Staffing + flexibility</div>
  <div class="brand"><span class="brand-dot"></span>Lanternis</div>
  <svg style="position:absolute;left:0;top:0" width="370" height="213" viewBox="0 0 370 213">
    <path d="M24 140 C40 110 55 80 70 110 C85 140 100 70 115 70 C128 70 128 140 140 150" fill="none" stroke="var(--navy)" stroke-width="1.2"/>
    <line x1="90" y1="92" x2="140" y2="92" stroke="var(--green)" stroke-width=".7"/>
    <polygon points="140,90 145,92 140,94" fill="var(--green)"/>
    <line x1="237" y1="90" x2="237" y2="170" stroke="#cfcfcf" stroke-width=".5"/>
    <g transform="translate(315,140)">
      <path d="M0 -32 A32 32 0 0 1 32 0 L20 0 A20 20 0 0 0 0 -20 Z" fill="var(--orange)"/>
      <path d="M32 0 A32 32 0 0 1 0 32 L0 20 A20 20 0 0 0 20 0 Z" fill="var(--blue)"/>
      <path d="M0 32 A32 32 0 0 1 -32 0 L-20 0 A20 20 0 0 0 0 20 Z" fill="var(--navy)"/>
      <path d="M-32 0 A32 32 0 0 1 0 -32 L0 -20 A20 20 0 0 0 -20 0 Z" fill="var(--green)"/>
      <g stroke="#fff" stroke-width="1.2"><line x1="0" y1="-33" x2="0" y2="-19"/><line x1="33" y1="0" x2="19" y2="0"/><line x1="0" y1="33" x2="0" y2="19"/><line x1="-33" y1="0" x2="-19" y2="0"/></g>
      <g fill="#fff" font-family="Ubuntu, sans-serif" font-size="8" text-anchor="middle"><text x="-17" y="-12">A</text><text x="18" y="-12">B</text><text x="-17" y="22">C</text><text x="18" y="22">D</text></g>
    </g>
  </svg>
  <div class="txt" style="left:150px;top:88px;color:var(--green);font-size:4.5px">Traffic changes during the day.<br>Flexibility is a must.</div>
  <div class="txt" style="left:155px;top:110px">How to create flexibility ?<br>By:
    <ul class="bullets" style="color:var(--blue)"><li>Blending</li><li>Part-timers</li><li>Split shift</li><li>Fillers</li><li>Homeworkers</li></ul></div>
  <div class="donut-label">BLENDING<br>OF TRAFFIC</div>
  <div class="footer"></div><div class="page-no">6</div>
</section>

<!-- 7 -->
<section class="slide s7">
  <div class="section-band">2.OPERATIONS</div>
  <div class="sub-band" style="width:120px">a. Staffing + flexibility</div>
  <div class="brand" style="right:auto;left:150px;top:52px"><span class="brand-dot"></span>Lanternis</div>
  <svg style="position:absolute;left:0;top:0" width="370" height="213" viewBox="0 0 370 213">
    <g stroke="var(--orange)" stroke-width=".8" fill="var(--orange)">
      <line x1="160" y1="72" x2="110" y2="92"/><polygon points="108,93 113,89 113,94"/>
      <line x1="220" y1="72" x2="262" y2="92"/><polygon points="264,93 259,89 259,94"/>
      <line x1="185" y1="168" x2="185" y2="182"/><polygon points="182,181 188,181 185,186"/>
    </g>
    <g stroke="var(--blue)" stroke-width=".8" fill="var(--blue)">
      <line x1="125" y1="108" x2="172" y2="128"/><polygon points="174,129 169,125 168,130"/>
      <line x1="255" y1="108" x2="202" y2="128"/><polygon points="200,129 205,125 206,130"/>
    </g>
  </svg>
  <div class="txt" style="left:80px;top:96px;font-size:6px">Technology Solutions</div>
  <div class="txt" style="left:248px;top:96px;font-size:6px">Services</div>
  <div class="txt" style="left:150px;top:128px;font-size:5px;color:var(--blue)">Efficient communication</div>
  <div class="cop">LANTERNIS= COP</div>
  <div class="cop-sub">Communication Optimization Partner</div>
  <div class="footer"></div><div class="page-no">7</div>
</section>

<!-- 8 -->
<section class="slide s8">
  <div class="section-band">2.OPERATIONS</div>
  <div class="sub-band" style="width:140px">b. Contact Center Organization.</div>
  <div class="brand"><span class="brand-dot"></span>Lanternis</div>
  <svg style="position:absolute;left:0;top:0" width="370" height="213" viewBox="0 0 370 213" font-family="Ubuntu, sans-serif">
    <circle cx="185" cy="76" r="16" fill="var(--green)"/>
    <text x="185" y="79" fill="#fff" font-size="8" text-anchor="middle">CCM</text>
    <rect x="93" y="98" width="185" height="9" fill="none" stroke="var(--green)" stroke-width=".8"/>
    <text x="185" y="104.5" fill="var(--ink)" font-size="4.5" text-anchor="middle">Training &amp; quality</text>
    <g font-size="5" fill="var(--ink)" text-anchor="middle">
      <ellipse cx="125" cy="122" rx="26" ry="8" fill="#e6e6e6" stroke="var(--red)" stroke-width=".6"/><text x="125" y="124">Supervisor</text>
      <line x1="108" y1="112" x2="140" y2="132" stroke="var(--red)" stroke-width="1.5"/>
      <ellipse cx="185" cy="122" rx="26" ry="8" fill="#e6e6e6" stroke="var(--red)" stroke-width=".6"/><text x="185" y="124">Supervisor</text>
      <line x1="168" y1="112" x2="200" y2="132" stroke="var(--red)" stroke-width="1.5"/>
      <ellipse cx="245" cy="122" rx="26" ry="8" fill="#e6e6e6" stroke="var(--red)" stroke-width=".6"/><text x="245" y="124">Supervisor</text>
      <line x1="228" y1="112" x2="260" y2="132" stroke="var(--red)" stroke-width="1.5"/>
    </g>
    <g fill="var(--blue)">
      <rect x="86" y="141" width="30" height="7"/><rect x="120" y="141" width="30" height="7"/><rect x="154" y="141" width="30" height="7"/>
      <rect x="188" y="141" width="30" height="7"/><rect x="222" y="141" width="30" height="7"/><rect x="256" y="141" width="30" height="7"/>
      <rect x="86" y="151" width="200" height="11"/>
    </g>
    <text x="88" y="146" fill="#fff" font-size="3">Teammanager</text>
    <text x="186" y="158.5" fill="#fff" font-size="5" text-anchor="middle">ADVISORS</text>
  </svg>
  <div class="footer"></div><div class="page-no">8</div>
</section>

</body>
</html>
```